Web Design Project

We need a design for the actual web.
http://mirela.vunto.example/
It will be a cakes and cupcakes online shop.

It is a one page site, with five anchors.

Inicio (Home)
Here it will show a brief explanation about our shop, just explaining we sell really nice cakes and cupcakes. Also we want to show a slide gallery, like the one it is working, but with not nice choosen pictures.

Productos/Tortas
This two anchors will be just one at the end, but I wanted to show the two options for accessing the different products, tabs or buttons. You can click on the firsts images on that links for see the "pop up image" with a better explanation of every product.

Contacto
Here it will show a little form, that will only appear in smartphones and maybe tablets, this form needs to be similar and much more simple than the principal form (the next anchor), so just focus on it once the next one its done.

Form
This will be the way the users will send the orders, its a complex form, focused on the UX. We dont want the user to type too much and we want it to surprise the user and fell really comfortable.

Industry/Entity Type

Tv

Requirements
Must have

• -Must have side menu, but you can redesign it completelly, but with the same structure
-Its important to focus all the content in the top and middle, we arent sure about users screens and it we set info at the footer, maybe its not gonna show (no scroll vertical).
-You can change all the colours of the site, we are open to new visions, you can surprise us.

```html
<!DOCTYPE html>
<html lang="es">
<head>
<meta charset="utf-8">
<title>Ovillo</title>
<link href="https://fonts.googleapis.com/css2?family=Niconne&family=Lato:wght@400;700&display=swap" rel="stylesheet">
<style>
  :root {
    --cream: #e6ddd2;
    --page: #ffffff;
    --brown: #5a3a24;
    --brown-dark: #40271a;
    --stitch: #e9dccd;
    --violet: #8a3fa8;
    --pink: #d9a9e6;
    --ink: #3b2a20;
    --caption: #f4efe8;
    --photo-light: #e9e4dc;
    --photo-dark: #6b5848;
  }
  * { margin: 0; padding: 0; box-sizing: border-box; }
  html, body { width: 1200px; height: 794px; overflow: hidden; }
  body {
    position: relative;
    font-family: "Lato", Helvetica, Arial, sans-serif;
    background: linear-gradient(to bottom, var(--cream) 0, var(--cream) 180px, #f1ece6 300px, var(--page) 460px);
  }
  .header-band {
    position: absolute; left: 0; top: 46px; width: 1200px; height: 134px;
    background: linear-gradient(to bottom, #65432b, var(--brown) 60%, var(--brown-dark));
  }
  .header-band .stitch {
    position: absolute; left: 0; width: 100%;
    border-top: 2px dashed var(--stitch); opacity: .8;
  }
  .stitch.top { top: 6px; }
  .stitch.bottom { bottom: 8px; }
  .brand {
    position: absolute; left: 158px; top: 14px; width: 192px; height: 192px;
    border-radius: 50%; background: var(--brown);
    border: 6px solid var(--page);
    box-shadow: 0 3px 6px rgba(0,0,0,.25);
    display: flex; align-items: center; justify-content: center;
  }
  .brand-name {
    font-family: "Lato", Helvetica, Arial, sans-serif;
    font-weight: 700; font-size: 36px; line-height: 1;
    color: var(--page); white-space: nowrap;
  }
  .social { position: absolute; top: 89px; display: flex; gap: 14px; left: 943px; }
  .social span {
    width: 44px; height: 44px; border-radius: 50%;
    background: #f3ede6; box-shadow: 0 2px 4px rgba(0,0,0,.3);
  }
  .side-menu { position: absolute; left: 158px; top: 225px; width: 222px; list-style: none; }
  .side-menu li {
    position: relative; height: 41px; margin-bottom: 2.5px;
    background: var(--brown-dark);
    clip-path: polygon(0 0, 100% 0, 94% 50%, 100% 100%, 0 100%);
    color: var(--page); font-size: 20px; line-height: 41px; padding-left: 14px;
  }
  .side-menu li.current { color: var(--pink); background: #4a2e1e; }
  .slider {
    position: absolute; left: 391px; top: 225px; width: 651px; height: 308px;
    overflow: hidden;
  }
  .slider .photo {
    position: absolute; inset: 0;
    background: radial-gradient(ellipse at 50% 35%, #fbf9f5 0, var(--photo-light) 30%, #b9aa98 60%, var(--photo-dark) 100%);
  }
  .caption {
    position: absolute; left: 0; top: 224px; width: 100%; height: 48px;
    background: rgba(244,239,232,.93);
    font-size: 22px; color: var(--ink); line-height: 48px; padding-left: 12px;
  }
  .price {
    position: absolute; left: 937px; top: 421px; width: 104px; height: 104px;
    border-radius: 50%; background: var(--brown);
    border: 5px solid var(--page);
    color: var(--page); font-size: 25px; text-align: center; line-height: 94px;
  }
  .dots { position: absolute; left: 286px; top: 284px; display: flex; gap: 8px; }
  .dots span { width: 15px; height: 15px; border-radius: 50%; border: 2px solid #fff; background: #b4aba2; }
  .dots span.on { background: #fff; box-shadow: inset 0 0 0 3px #8d8279; }
  .intro { position: absolute; left: 434px; top: 560px; width: 566px; color: var(--ink); }
  .intro h1 {
    font-family: "Niconne", cursive; font-weight: 400; font-size: 33px;
    color: var(--violet); text-align: center; margin-bottom: 22px; margin-left: -20px;
  }
  .intro p { font-size: 14.5px; line-height: 20px; margin-bottom: 20px; text-align: justify; }
</style>
</head>
<body>
  <header class="header-band">
    <div class="stitch top"></div>
    <div class="stitch bottom"></div>
  </header>
  <div class="brand"><span class="brand-name">Ovillo</span></div>
  <div class="social" aria-label="Redes sociales"><span></span><span></span></div>

  <ul class="side-menu">
    <li class="current">Inico</li>
    <li>Productos \ Tortas</li>
    <li>Contacto</li>
    <li>Form</li>
  </ul>

  <section class="slider">
    <div class="photo" role="img" aria-label="Fotografía de cupcakes con crema blanca"></div>
    <div class="caption">Cupcakes' name</div>
    <div class="dots"><span class="on"></span><span></span><span></span></div>
  </section>
  <div class="price">$19.00</div>

  <main class="intro">
    <h1>Los mejores Cupcakes y Pasteles de Santiago!</h1>
    <p>Finalmente ya está disponible en <strong>Santiago de Chile</strong> nuestro catálogo de sabrosos Cupcakes y Tortas.</p>
    <p>Con ingredientes <strong>100% naturales</strong> y elaborados artesanalmente.</p>
    <p>No solo hay que tener en cuenta la presentación fabulosa de los mismos, lo que más destacan nuestros clientes es el sabor <strong>exquisito</strong> y la textura.</p>
  </main>
</body>
</html>
```